Mini-Banner für Rubriken
Hallo,
wir benötigen für unsere Seite www.quilmar.de neue und vorallem passende Banner für die Highlights (rechte Seite) innerhalb der Rubriken, wie z.B. All Inklusive, Wellness, Urlaub an der Küste u.s.w. Vielen Dank für die Vorschläge !

```html
<!DOCTYPE html>
<html lang="de">
<head>
<meta charset="utf-8">
<title>Mini-Banner für Rubriken – Entwurf 2</title>
<link href="https://fonts.googleapis.com/css2?family=Noto+Sans:wght@400;700&family=Roboto+Condensed:wght@700&family=Barlow+Semi+Condensed:wght@700&display=swap" rel="stylesheet">
<style>
  :root {
    --page-bg: #ffffff;
    --box-bg: #f4f4f4;
    --box-border: #d6d6d6;
    --box-head: #e6e6e6;
    --text: #333333;
    --muted: #555555;
    --accent-red: #9b1b1b;
    --price-red: #b01010;
    --button-red: #8e1d1d;
    --rule: #555555;
    --ring-blue: #0f6fc0;
    --ring-green: #86c232;
    --lens-bg: #fcfcfc;
    --strip-blue: #1b5fb8;
    --strip-red: #d42020;
    --strip-green: #5a7a1c;
    --strip-gold: #e3a21a;
    --ink: #161616;
  }
  * { box-sizing: border-box; margin: 0; padding: 0; }
  html, body { width: 1200px; height: 910px; overflow: hidden; background: var(--page-bg); }
  body { font-family: "Noto Sans", sans-serif; color: var(--text); }

  .stage { position: relative; width: 931px; height: 706px; transform: scale(1.2889); transform-origin: 0 0; overflow: hidden; background: var(--page-bg); }

  .abs { position: absolute; }
  .box { position: absolute; background: var(--box-bg); border: 1px solid var(--box-border); border-radius: 3px; overflow: hidden; }
  .box-head { background: linear-gradient(#ededed, #dcdcdc); border-bottom: 1px solid var(--box-border); height: 23px; line-height: 23px; text-align: center; font-size: 12px; font-weight: 700; color: #222; }
  .box-body { padding: 8px 7px; font-size: 11.5px; line-height: 1.2; color: var(--text); }

  .link-list { list-style: none; font-size: 11.5px; line-height: 14px; color: var(--accent-red); }
  .link-list li::before { content: "• "; }

  .btn { position: absolute; background: linear-gradient(#a3302f, var(--button-red)); color: #fff; font-size: 12px; font-weight: 700; text-align: center; line-height: 19px; height: 19px; border-radius: 2px; }

  .photo { position: absolute; border-radius: 3px; }
  .rule { position: absolute; height: 2px; background: var(--rule); left: 222px; width: 485px; }

  .price-label { font-size: 12px; font-weight: 700; color: var(--price-red); }
  .price { font-size: 18px; font-weight: 700; color: var(--price-red); }

  .listing-title { font-size: 14px; font-weight: 700; color: var(--accent-red); }
  .listing-sub { font-size: 12px; font-weight: 700; color: var(--accent-red); }
  .listing-text { font-size: 11.5px; line-height: 14.5px; color: var(--muted); }

  /* Rubrik banners */
  .banner { position: absolute; width: 186px; height: 60px; border: 1px solid #555; overflow: hidden; }
  .banner-visual { position: absolute; inset: 0 0 11px 0; }
  .banner-strip { position: absolute; left: 0; right: 0; bottom: 0; height: 11px; font-family: "Roboto Condensed", sans-serif; font-weight: 700; font-size: 9.5px; line-height: 11px; color: #fff; text-align: right; padding-right: 4px; letter-spacing: 0.3px; text-transform: uppercase; }
  .banner--wellness .banner-visual { background: linear-gradient(100deg, #7a4a2e 0%, #c98a62 40%, #e8c3a4 70%, #b07a56 100%); }
  .banner--wellness .banner-strip { background: var(--strip-blue); }
  .banner--allinclusive .banner-visual { background: linear-gradient(180deg, #9fc2dc 0%, #cfdde6 30%, #6f8f5a 55%, #3f6a3a 100%); }
  .banner--allinclusive .banner-strip { background: var(--strip-red); }
  .banner--harz .banner-visual { background: linear-gradient(180deg, #a9cde8 0%, #dbe9f0 35%, #7fa04a 60%, #3e6421 100%); }
  .banner--harz .banner-strip { background: var(--strip-green); }
  .banner--coast .banner-visual { background: linear-gradient(180deg, #3d7fc6 0%, #8fbde6 40%, #6a8e6a 60%, #2f6f9c 80%, #c9b58a 100%); }
  .banner--coast .banner-strip { background: var(--strip-gold); }
  .badge { position: absolute; left: 6px; top: 4px; width: 34px; height: 34px; border-radius: 50%; background: #d81e1e; border: 1.5px solid #fff; color: #fff; font-family: "Roboto Condensed", sans-serif; font-weight: 700; text-align: center; line-height: 1; padding-top: 8px; }
  .badge-big { display: block; font-size: 10px; }
  .badge-small { display: block; font-size: 5.5px; margin-top: 1px; }

  .lens-title { position: absolute; left: 240px; top: 482px; width: 318px; text-align: center; font-family: "Barlow Semi Condensed", sans-serif; font-weight: 700; font-size: 35px; color: var(--ink); letter-spacing: 1px; }

  .input { position: absolute; height: 17px; background: #fff; border: 1px solid #888; }
  .search-btn { position: absolute; background: #fff; border: 1px solid #bbb; font-size: 12px; text-align: center; line-height: 19px; }
</style>
</head>
<body>
<div class="stage">

  <!-- Left column -->
  <div class="box" style="left:8px; top:-12px; width:188px; height:69px;">
    <ul class="link-list" style="padding:6px 7px;">
      <li>Fest &amp; Feiertage</li>
      <li>love &amp; romance</li>
    </ul>
    <ul class="link-list" style="padding:0 7px;">
      <li style="margin-top:4px;">Alle Angebote</li>
    </ul>
  </div>

  <div class="box" style="left:8px; top:70px; width:188px; height:127px;">
    <div class="box-head">Gutschein schenken</div>
    <div class="photo" role="img" aria-label="Rote Gutscheinkarte mit Schriftzug Gutschein" style="left:1px; top:25px; width:184px; height:93px; border-radius:0; background:linear-gradient(135deg,#7d1015,#b4232a 50%,#8a141a);"></div>
  </div>

  <div class="box" style="left:8px; top:208px; width:188px; height:74px;">
    <div class="box-head"></div>
    <ul class="link-list" style="padding:8px 7px;">
      <li>Rückruf anfordern</li>
      <li>Anfrage stellen</li>
    </ul>
  </div>

  <div class="box" style="left:8px; top:294px; width:188px; height:191px;">
    <div class="box-head">Newsletter</div>
    <div class="box-body" style="padding-top:22px; line-height:13px;">Bleiben Sie immer auf dem neuesten Stand. Tragen Sie sich jetzt für unseren Newsletter ein.</div>
    <div class="abs" style="left:7px; top:110px; font-size:11.5px;">Email:</div>
    <div class="input" style="left:43px; top:108px; width:140px;"></div>
    <div class="btn" style="left:50px; top:130px; width:130px;">Eintragen</div>
    <div class="abs" style="left:43px; top:164px; font-size:11.5px; color:var(--accent-red);">Newsletter Abstellen</div>
  </div>

  <div class="box" style="left:8px; top:497px; width:188px; height:220px;">
    <div class="box-head">VIP Programm</div>
    <div class="box-body" style="line-height:13.5px; padding-top:20px;">
      <p>Bei einer Buchung erhalten Sie exklusive Sonder-konditionen und verschiedene kostenfreie Upgrades als quilmar.de Kunde.</p>
      <p style="margin-top:13px;">Legen Sie einfach bei Anreise im Hotel Ihre quilmar.de - VIP-Karte vor. Diese erhalten Sie mit Ihren Buchungs-unterlagen.</p>
    </div>
    <div class="photo" role="img" aria-label="VIP-Karte" style="left:7px; top:197px; width:172px; height:20px; background:linear-gradient(#e8c98a,#c9a25a);"></div>
  </div>

  <!-- Middle column -->
  <div class="photo" role="img" aria-label="Festlich gedeckter Hotelrestaurant-Saal" style="left:228px; top:-5px; width:218px; height:95px; background:linear-gradient(160deg,#6b3b22,#c38a52 45%,#a8442c 70%,#e7d6c4);"></div>
  <div class="abs listing-text" style="left:483px; top:-2px; width:215px;">entspricht den Erwartungen eines 4 Sterne Hauses. Gro…</div>
  <div class="abs" style="left:486px; top:44px;"><span class="price-label">schon ab</span>&nbsp;&nbsp;&nbsp;<span class="price">199,00 € p.P.</span></div>
  <div class="btn" style="left:570px; top:70px; width:124px;">mehr Infos...!</div>
  <div class="rule" style="top:109px;"></div>

  <div class="abs listing-title" style="left:229px; top:122px;">Ba</div>
  <div class="abs listing-sub" style="left:560px; top:141px;">landschaft</div>
  <div class="rule" style="top:332px;"></div>

  <div class="abs listing-title" style="left:650px; top:381px;">lose</div>
  <div class="abs listing-text" style="left:654px; top:440px;">genau<br>und Feld,<br>see und</div>
  <div class="abs price" style="left:592px; top:506px;">,77 € p.P.</div>
  <div class="btn" style="left:570px; top:535px; width:124px;">mehr Infos...!</div>
  <div class="rule" style="top:563px;"></div>

  <div class="abs listing-title" style="left:229px; top:587px;">Wochenend-A&nbsp;&nbsp;&nbsp;&nbsp;&nbsp;&nbsp;&nbsp;&nbsp;&nbsp;&nbsp;&nbsp;&nbsp;&nbsp;&nbsp;&nbsp;&nbsp;konditionen in der Altmark</div>
  <div class="abs listing-sub" style="left:229px; top:605px;">2 ÜN von Freitag bis Sonntag inklusive Vollverpflegung &amp; Getränke</div>
  <div class="abs listing-text" style="left:231px; top:636px; width:215px;">Ein paar romantische Tage bringen Ihnen die gewünschte Entspannung. Im Einklang die Natur erleben. Spüren Sie die wohltuende Natur bei ausgedehnten …</div>
  <div class="photo" role="img" aria-label="Hotelrestaurant mit gedeckten Tischen" style="left:459px; top:634px; width:214px; height:80px; background:linear-gradient(170deg,#d8d2c2,#8f8a78 50%,#4a4236);"></div>

  <!-- Right column -->
  <div class="box" style="left:730px; top:-10px; width:188px; height:46px; background:#fff; border-color:#ddd;">
    <div class="abs" style="left:12px; top:6px; width:137px; height:3px; background:var(--accent-red);"></div>
    <div class="search-btn" style="left:12px; top:13px; width:160px; height:22px;">suchen</div>
  </div>

  <div class="box" style="left:730px; top:67px; width:188px; height:298px;">
    <div class="box-head">Highlights</div>
  </div>
  <div class="banner banner--wellness" style="left:731px; top:95px;">
    <div class="banner-visual" role="img" aria-label="Frau bei einer Wellness-Massage"></div>
    <div class="banner-strip">Wellness Urlaub in Bayern</div>
  </div>
  <div class="banner banner--allinclusive" style="left:731px; top:159px;">
    <div class="banner-visual" role="img" aria-label="Bergsee im Erzgebirge"></div>
    <div class="badge"><span class="badge-big">ALL</span><span class="badge-small">INCLUSIVE</span></div>
    <div class="banner-strip">im Erzgebirge</div>
  </div>
  <div class="banner banner--harz" style="left:731px; top:223px;">
    <div class="banner-visual" role="img" aria-label="Grüne Hügellandschaft im Harz"></div>
    <div class="banner-strip">Erholung im Harz</div>
  </div>
  <div class="banner banner--coast" style="left:731px; top:287px;">
    <div class="banner-visual" role="img" aria-label="Hafen mit Palmen an der Küste"></div>
    <div class="banner-strip">Urlaub an der Küste</div>
  </div>

  <div class="box" style="left:730px; top:378px; width:188px; height:224px;">
    <div class="box-head">quilmar Telefon Support</div>
    <div class="box-body" style="line-height:13.5px; padding-top:10px;">
      <p>Sie möchten dieses Angebot telefonisch buchen oder wünschen eine persönliche Beratung? Sie erreichen uns von Montag-Freitag von 08:00 - 17:00 Uhr</p>
      <p style="margin-top:14px;">unter</p>
      <p style="margin-top:14px; font-weight:700;">quilmar <span style="color:var(--price-red);">FREECALL</span><br>(D) 0800 - 12 34 567<br>oder per Email<br><span style="color:var(--price-red);">info@quilmar.de</span></p>
    </div>
  </div>

  <div class="box" style="left:730px; top:615px; width:188px; height:110px;">
    <div class="box-head">Hotel Übersicht</div>
    <div class="photo" role="img" aria-label="Karte Deutschlands mit Hotelstandorten" style="left:8px; top:33px; width:170px; height:70px; border-radius:0; background:linear-gradient(#f2f2f2,#d9d9d9);"></div>
  </div>

  <!-- Magnifier callout -->
  <svg class="abs" style="left:0; top:0;" width="931" height="706" viewBox="0 0 931 706" aria-hidden="true">
    <polygon points="578,190 729,127 660,285" fill="var(--ring-blue)"/>
    <circle cx="399" cy="397" r="259" fill="var(--ring-blue)"/>
    <circle cx="399" cy="397" r="245" fill="var(--ring-green)"/>
    <circle cx="399" cy="397" r="233" fill="var(--lens-bg)"/>
  </svg>

  <div class="banner banner--wellness" style="left:305px; top:198px; width:187px;">
    <div class="banner-visual" role="img" aria-label="Frau bei einer Wellness-Massage"></div>
    <div class="banner-strip">Wellness Urlaub in Bayern</div>
  </div>
  <div class="banner banner--allinclusive" style="left:305px; top:263px; width:187px;">
    <div class="banner-visual" role="img" aria-label="Bergsee im Erzgebirge"></div>
    <div class="badge"><span class="badge-big">ALL</span><span class="badge-small">INCLUSIVE</span></div>
    <div class="banner-strip">im Erzgebirge</div>
  </div>
  <div class="banner banner--harz" style="left:305px; top:328px; width:187px;">
    <div class="banner-visual" role="img" aria-label="Grüne Hügellandschaft im Harz"></div>
    <div class="banner-strip">Erholung im Harz</div>
  </div>
  <div class="banner banner--coast" style="left:305px; top:393px; width:187px;">
    <div class="banner-visual" role="img" aria-label="Hafen mit Palmen an der Küste"></div>
    <div class="banner-strip">Urlaub an der Küste</div>
  </div>

  <div class="lens-title">ENTWURF 2</div>
</div>
</body>
</html>
```